Online Digital Solutions Agency needs a New Business Card

We are a Online/Digital solution agency. We provide WordPress Solutions, Online & Digital Marketing Solutions including SEO, Social Media Marketing and Managed Hosting including VPS and Cloud Hosting solutions. We also design and build bespoke web sites and web applications for various clients. We are very good at site migrations, 3rd party API integrations and mobile app development.

We are rebranding our agency and have already designed a new logo. We have selected 5-6 colours as our base colour and are currently building our new website based around these colour scheme.

Our logo indicates that we are a cloud solution providers, and (i.e. the Clouds), and developers (i.e. HTML Tags, and CSS formats). We use the 5-6 base colours and use various shades of these colours as required.

Our old website is located at: www.brambleforgelabs.com

And our new website is going to be at (we are working on it at the moment ...):
https://creative.brambleforgelabs.co.uk/

Our slogan is "Digital Transformation Specialist"

What we mean by that is; we can take any existing business and get them up and transform them in to the digital world, starting with Hosting, Web Design, Development & Online Marketing aspects.

The powerpoint is a document that we use to present our projects to clients at the moment, and the cloud is on the background as we clarified earlier. (Just to get the idea)

What we are looking for is a Great WoW factor design to start with, ideally with the Logo and Logo colour scheme if possible but not required as long as the designers can do better, and basically give life to our logo and company via the Business card design.

Ideally with some icons perhaps to indicate the address, location, mobile, email, and website would be good but again optional as long as there is a good design.

The cloud can be used as a background if required in a light shade or as a watermark share perhaps.

The logos' and the Illustrator files are shared with you so you can use them as required.

Ideally the business card should have a Name, title, Mobile, Email , Website, Address and perhaps some social media links.

Target Market(s)

New Startups, SME's, Contract and Outsource Clients

Contact Information for Business Card

Company Name:
==============
BrambleForge Labs (UK) Ltd.

Tag Line:
========
“Digital Transformation Specialists”

Adress:
=======

Suite KR73054
14-16 Ashgrove Lane
London
E9 4PD.

Name:
=====
Idris Malek

Title: (Optional)
=============
FQTA, PgD (RNOM)

Role:
=====
Digital Solutions Architect

Email:
=====
idris@brambleforgelabs.uk

WebSite:
=======
http://www.brambleforgelabs.uk

OR

www.brambleforgelabs.uk

Mobile:
======
0044 (0)75 218 30479

OR

+44 (0)75 218 30479

LinkedIN: (Optional)
========
https://uk.linkedin.com/in/idrismalek

Skype: (Optional)
======
idris.malek

Twitter (Optional) : idrismalek

Font styles to use
Serif
Sans Serif

Requirements
Must have
• The Logo
• Business Name
• Person Name
• Title
• Mobile
• Email
• Website
• Address
• I have provided the colour scheme on my files.
Nice to have
• Twiter
• Linked in
• Facebook

```html
<!DOCTYPE html>
<html lang="en">
<head>
<meta charset="utf-8">
<title>BrambleForge Labs – Business Card</title>
<link rel="stylesheet" href="https://fonts.googleapis.com/css2?family=Source+Sans+3:wght@400;600;700&display=swap">
<style>
  :root {
    --backdrop: #a3a3a3;
    --card-white: #ffffff;
    --brand-blue: #0b4f9e;
    --brand-blue-deep: #0a55a6;
    --ink: #1d1d1f;
    --divider: #d9d9d9;
    --shadow: rgba(0, 0, 0, 0.35);
  }
  html, body {
    margin: 0;
    padding: 0;
    width: 1200px;
    height: 802px;
    overflow: hidden;
    background: var(--backdrop);
    font-family: "Source Sans 3", Arial, sans-serif;
  }
  .stage {
    position: relative;
    width: 1200px;
    height: 802px;
  }
  .card {
    position: absolute;
    top: 274px;
    width: 442px;
    height: 265px;
    box-shadow: 2px 3px 6px var(--shadow);
  }
  .card--front { left: 136px; background: var(--card-white); }
  .card--back  { left: 624px; background: var(--brand-blue-deep); }

  .brand {
    position: absolute;
    left: 10px;
    top: 124px;
    width: 204px;
    text-align: center;
  }
  .brand__name {
    display: inline-flex;
    align-items: center;
    gap: 6px;
    font-size: 20px;
    font-weight: 700;
    color: var(--brand-blue);
    line-height: 1;
    white-space: nowrap;
  }
  .brand__dot {
    width: 9px;
    height: 9px;
    border-radius: 50%;
    background: var(--brand-blue);
    flex: none;
  }
  .brand__tagline {
    margin-top: 12px;
    font-size: 8.5px;
    font-weight: 600;
    letter-spacing: 0.2px;
    color: var(--brand-blue);
    white-space: nowrap;
  }

  .divider {
    position: absolute;
    left: 226px;
    top: 67px;
    width: 1px;
    height: 130px;
    background: var(--divider);
  }

  .contact {
    position: absolute;
    left: 240px;
    top: 76px;
    color: var(--ink);
  }
  .contact__name {
    margin: 0;
    font-size: 19px;
    font-weight: 600;
    color: var(--brand-blue);
    line-height: 1;
  }
  .contact__role {
    margin: 1px 0 9px 1px;
    font-size: 12.5px;
    line-height: 1.1;
  }
  .contact__list {
    list-style: none;
    margin: 0;
    padding: 0;
  }
  .contact__item {
    display: flex;
    align-items: center;
    gap: 4px;
    font-size: 12px;
    line-height: 15.7px;
    white-space: nowrap;
  }
  .contact__icon {
    width: 11px;
    height: 11px;
    fill: var(--brand-blue);
    flex: none;
  }
  .contact__address {
    margin: 7px 0 0 0;
    font-style: normal;
    font-size: 12px;
    line-height: 16px;
    white-space: nowrap;
  }

  .back-brand {
    position: absolute;
    right: 28px;
    top: 150px;
    font-size: 16px;
    font-weight: 700;
    color: var(--card-white);
    white-space: nowrap;
  }
</style>
</head>
<body>
<main class="stage">
  <section class="card card--front" aria-label="Business card front">
    <div class="brand">
      <div class="brand__name"><span class="brand__dot"></span>BrambleForge Labs</div>
      <div class="brand__tagline">{ BUILD : HOST : GROW WITH CODE CRAFT }</div>
    </div>

    <div class="divider"></div>

    <div class="contact">
      <h1 class="contact__name">Idris Malek</h1>
      <p class="contact__role">Digital Solutions Architect</p>
      <ul class="contact__list">
        <li class="contact__item">
          <svg class="contact__icon" viewBox="0 0 12 12" aria-hidden="true"><path d="M1 4.5C1 3 3 2 6 2s5 1 5 2.5v1H8.5V4.2C7.7 4 4.3 4 3.5 4.2v1.3H1z"/><path d="M2.5 6.5h7l1 4h-9z"/></svg>
          +44 (0)75 218 30479
        </li>
        <li class="contact__item">
          <svg class="contact__icon" viewBox="0 0 12 12" aria-hidden="true"><path d="M3.5 0.5h5a1 1 0 0 1 1 1v9a1 1 0 0 1-1 1h-5a1 1 0 0 1-1-1v-9a1 1 0 0 1 1-1zm0.3 1.3v7.4h4.4V1.8z"/></svg>
          0044 (0)75 218 30479
        </li>
        <li class="contact__item">
          <svg class="contact__icon" viewBox="0 0 12 12" aria-hidden="true"><path d="M1 3h10v6.5H1zm1 1.1v0.3l4 2.6 4-2.6v-0.3z"/></svg>
          idris@brambleforgelabs.uk
        </li>
        <li class="contact__item">
          <svg class="contact__icon" viewBox="0 0 12 12" aria-hidden="true"><circle cx="6" cy="6" r="5.2"/><path d="M4 3.5c1 .3 1.5 1 1 1.8-.6.8.3 1.3 1 1.5.6.3.3 1.4-.3 2.2" stroke="#fff" stroke-width="1" fill="none"/></svg>
          www.brambleforgelabs.uk
        </li>
      </ul>
      <address class="contact__address">
        14-16, Ashgrove Lane<br>
        London,E9 4PD United Kingdom
      </address>
    </div>
  </section>

  <section class="card card--back" aria-label="Business card back">
    <div class="back-brand">BrambleForge Labs</div>
  </section>
</main>
</body>
</html>
```